3" Round Business Card for Funeral Home

We need a business card designed for our cremation service. We would like to use a 3" round business card.

The business card will be 2-sided. One side with the logo featured prominently. The back sad will have employee name and contact info.

Templates for printing have been attached to project as well as logo

We like soft colors like the logo. Final design should promote a feeling of trust.

Industry/Entity Type

Funeral

Contact Information for Business Card

Employee Name, Phone number, email, web address

Requirements
Should not have
• any sort of funeral item such as urn, casket, hearse, tombstone

```html
<!DOCTYPE html>
<html lang="en">
<head>
<meta charset="utf-8">
<title>Stillwater Care – Round Business Card</title>
<link href="https://fonts.googleapis.com/css2?family=Mulish:wght@400;700&display=swap" rel="stylesheet">
<style>
  :root {
    --backdrop: #5a5b5d;
    --card-white: #ffffff;
    --teal: #10a89e;
    --plum: #8b2b8c;
    --text-light: #ffffff;
    --label-tint: #bfe8e3;
  }
  html, body {
    margin: 0;
    padding: 0;
    width: 1200px;
    height: 1000px;
    overflow: hidden;
    background: var(--backdrop);
    font-family: "Mulish", "Century Gothic", sans-serif;
  }
  .canvas {
    position: relative;
    width: 1200px;
    height: 1000px;
  }
  .card {
    position: absolute;
    top: 229px;
    width: 546px;
    height: 546px;
    border-radius: 50%;
    box-shadow: 8px 12px 22px rgba(0, 0, 0, 0.28);
    overflow: hidden;
  }
  .card--front {
    left: 45px;
    background: var(--card-white);
  }
  .card--back {
    left: 611px;
    background: var(--teal);
  }
  .brand-name {
    position: absolute;
    left: 0;
    right: 0;
    top: 240px;
    text-align: center;
    font-size: 40px;
    font-weight: 400;
    color: var(--teal);
    letter-spacing: 0.2px;
    padding-right: 8px;
  }
  .connector {
    position: absolute;
    top: 287px;
    height: 3px;
    background: var(--plum);
  }
  .card--front .connector {
    left: 480px;
    width: 70px;
  }
  .card--back .connector {
    left: 0;
    width: 86px;
  }
  .contact {
    position: absolute;
    left: 102px;
    top: 232px;
    color: var(--text-light);
  }
  .contact__name {
    margin: 0 0 20px;
    font-size: 21px;
    font-weight: 700;
    letter-spacing: 0.3px;
  }
  .contact__list {
    list-style: none;
    margin: 0;
    padding: 0;
    font-size: 21px;
    line-height: 32.5px;
    font-weight: 400;
  }
  .contact__label {
    display: inline-block;
    width: 24px;
    color: var(--label-tint);
  }
</style>
</head>
<body>
  <main class="canvas">
    <section class="card card--front" aria-label="Card front">
      <div class="brand-name">stillwatercare.com</div>
      <span class="connector"></span>
    </section>

    <section class="card card--back" aria-label="Card back">
      <span class="connector"></span>
      <div class="contact">
        <h1 class="contact__name">DANIEL REYES</h1>
        <ul class="contact__list">
          <li><span class="contact__label">P</span>: +1.510.555.0148</li>
          <li><span class="contact__label">E</span>: daniel@stillwatercare.com</li>
          <li><span class="contact__label">W</span>: www.stillwatercare.com</li>
        </ul>
      </div>
    </section>
  </main>
</body>
</html>
```